Coastal Fern Grounds SVCS LLC

We need a wrap for my 2019 Vordel 2600 Grand Cab & Trailer Wrap for our landscaping company, I want it look Patriotic All my trucks, trailers and vans will be wrapped the same way!! Were based out of Fort Myers, FL . We are a State Certified Irrigation & Landscaping Contractor: License# 648207315
The services we offer: (Irrigation, Maintenance Programs, Landscape Design & Installation, Landscape Lighting, Well Pump, Drainage Systems) We would like a wrap that is beautiful, not too crowded, something that's going to make us really stand out from the crowd. Something that is very eye catching! Please be very creative. This wrap will be going on my (2019 VORDEL 2600 GRAND CAB) & (ENCLOSED TRAILER: 14' long x 7’ wide 6' high ) Please be creative you can use a mixture of whatever colors you think are going to look good from the color that I picked out if you don’t think we need to use them all that’s OK just use whatever is going to look good professional but also pop out!

Target Market(s)

40 years old and up

Industry/Entity Type

Landscape Design & Install, Irrigation, Landscape Lighting, Drainage systems, Well Pump

Colors
0054AA
0677BA
7BADD7
CADEEF
E8F1F8
00AB8E
00BBA5
67D7C9
C6EFE9
E9F9F6
EB3D1F
EC4F4E
F09395
F8D3D4
FCEDEE

Requirements
Must have
• Colors: ( Heather Gray, Red, Blue, Beautiful darker green like grass color Green ). logo real big, with a very UNIQUE custom design AROUND LOGO MY STATE CERTIFIED LICENSE #648207315- 555-316-7024. Cfglawnworks.example. HIGHLY RATED ON SEEKWELL & BRENDA’S ROSTER!
Should not have
• NO BIG OF LANDSCAPES! PLEASE REFER TO EXAMPLES!!

```html
<!DOCTYPE html>
<html lang="en">
<head>
<meta charset="utf-8">
<title>Coastal Fern Grounds SVCS LLC — Trailer Wrap</title>
<link rel="stylesheet" href="https://fonts.googleapis.com/css2?family=Montserrat:wght@700;800;900&display=swap">
<style>
  :root {
    --canvas: #e9ecef;
    --brand-blue: #1f5aa8;
    --patriot-red: #d8321c;
    --grass-dark: #0f4d22;
    --grass-mid: #1f6e34;
    --grass-light: #3f9a3c;
    --band-green: #155c2b;
    --white: #ffffff;
    --garden-a: #6b8f3a;
    --garden-b: #b59a6a;
    --garden-c: #58a63c;
    --house-a: #8fb0c8;
    --house-b: #7a9a58;
    --house-c: #4fa834;
  }
  html, body {
    margin: 0;
    padding: 0;
    width: 1200px;
    height: 658px;
    overflow: hidden;
    background: var(--canvas);
  }
  .wrap-panel {
    position: absolute;
    left: 20px;
    top: 55px;
    width: 1160px;
    height: 548px;
    overflow: hidden;
    background: var(--grass-mid);
  }
  .wrap-art {
    position: absolute;
    inset: 0;
    width: 100%;
    height: 100%;
  }
  .brand-block {
    position: absolute;
    left: 0;
    top: 32px;
    width: 540px;
    height: 176px;
    display: flex;
    align-items: center;
    justify-content: center;
    gap: 18px;
  }
  .brand-mark {
    width: 74px;
    height: 74px;
    border-radius: 50%;
    background: var(--patriot-red);
    flex: none;
  }
  .brand-name {
    margin: 0;
    font-family: "Montserrat", sans-serif;
    font-weight: 900;
    color: var(--brand-blue);
    text-align: center;
    line-height: 1.05;
    text-transform: uppercase;
  }
  .brand-name .primary {
    display: block;
    font-size: 40px;
    letter-spacing: 1px;
  }
  .brand-name .secondary {
    display: flex;
    align-items: center;
    justify-content: center;
    gap: 10px;
    font-size: 18px;
    letter-spacing: 3px;
    margin-top: 8px;
  }
  .brand-rule {
    display: block;
    width: 34px;
    height: 3px;
    background: var(--patriot-red);
  }
  .service-list {
    position: absolute;
    left: 78px;
    top: 240px;
    margin: 0;
    padding: 0;
    list-style: none;
    font-family: "Montserrat", sans-serif;
    font-weight: 800;
    font-size: 26px;
    letter-spacing: 1px;
    color: var(--white);
    text-transform: uppercase;
  }
  .service-item {
    display: flex;
    align-items: center;
    gap: 12px;
    height: 35px;
  }
  .service-item:nth-child(2) { margin-left: 2px; }
  .service-item:nth-child(3) { margin-left: 4px; }
  .service-item:nth-child(4) { margin-left: 6px; }
  .service-item:nth-child(5) { margin-left: 8px; }
  .tick-icon {
    width: 26px;
    height: 26px;
    flex: none;
  }
  .contact-block {
    position: absolute;
    left: 78px;
    top: 432px;
    width: 440px;
    font-family: "Montserrat", sans-serif;
    font-weight: 700;
    color: var(--white);
    text-transform: uppercase;
  }
  .license-line {
    display: inline-block;
    margin: 0 0 8px;
    padding: 4px 10px;
    background: var(--patriot-red);
    font-size: 14px;
    letter-spacing: 1px;
  }
  .contact-line {
    margin: 0 0 6px;
    font-size: 18px;
    font-weight: 800;
    letter-spacing: 0.5px;
  }
  .contact-line .web { text-transform: none; }
  .rating-line {
    margin: 0;
    font-size: 13px;
    letter-spacing: 0.5px;
  }
</style>
</head>
<body>
  <main class="wrap-panel">
    <svg class="wrap-art" viewBox="0 0 1160 548" xmlns="http://www.w3.org/2000/svg">
      <defs>
        <linearGradient id="shrub-fill" x1="0" y1="0" x2="0" y2="1">
          <stop offset="0" stop-color="var(--grass-dark)"/>
          <stop offset="0.6" stop-color="var(--grass-mid)"/>
          <stop offset="1" stop-color="var(--grass-light)"/>
        </linearGradient>
        <linearGradient id="garden-fill" x1="0" y1="0" x2="1" y2="1">
          <stop offset="0" stop-color="var(--garden-a)"/>
          <stop offset="0.5" stop-color="var(--garden-b)"/>
          <stop offset="1" stop-color="var(--garden-c)"/>
        </linearGradient>
        <linearGradient id="lawn-fill" x1="0" y1="0" x2="0" y2="1">
          <stop offset="0" stop-color="var(--grass-mid)"/>
          <stop offset="1" stop-color="var(--house-c)"/>
        </linearGradient>
        <linearGradient id="house-fill" x1="0" y1="0" x2="0" y2="1">
          <stop offset="0" stop-color="var(--house-a)"/>
          <stop offset="0.55" stop-color="var(--house-b)"/>
          <stop offset="1" stop-color="var(--house-c)"/>
        </linearGradient>
      </defs>

      <rect class="shrub-backdrop" x="0" y="0" width="1160" height="548" fill="url(#shrub-fill)"
            role="img" aria-label="Photo of dense green shrubs and hedges"/>

      <rect class="top-band" x="0" y="0" width="560" height="32" fill="var(--band-green)"/>
      <rect class="brand-band" x="0" y="32" width="560" height="176" fill="var(--white)"/>

      <path class="garden-photo" d="M 560 0 C 470 150 480 400 700 548 L 1160 548 L 1160 0 Z"
            fill="url(#garden-fill)" stroke="var(--white)" stroke-width="8"
            role="img" aria-label="Photo of a winding stone garden wall with colourful planting beds"/>

      <path class="lawn-leaf" d="M 600 0 C 575 170 600 350 645 440 C 720 300 715 140 620 0 Z"
            fill="url(#lawn-fill)" stroke="var(--white)" stroke-width="7"
            role="img" aria-label="Photo of a green lawn bordered by yellow shrubs"/>

      <path class="house-photo" d="M 760 0 C 870 140 820 430 985 548 L 1160 548 L 1160 0 Z"
            fill="url(#house-fill)" stroke="var(--white)" stroke-width="8"
            role="img" aria-label="Photo of a stone house with flowering shrubs, boulders and a river rock bed"/>
    </svg>

    <header class="brand-block">
      <span class="brand-mark" aria-hidden="true"></span>
      <h1 class="brand-name">
        <span class="primary">Coastal Fern</span>
        <span class="secondary"><span class="brand-rule"></span>Grounds SVCS LLC<span class="brand-rule"></span></span>
      </h1>
    </header>

    <ul class="service-list">
      <li class="service-item">
        <svg class="tick-icon" viewBox="0 0 26 26"><circle cx="13" cy="13" r="10.5" fill="none" stroke="var(--white)" stroke-width="3"/><path d="M7.5 13.5 L12 18 L21 6" fill="none" stroke="var(--white)" stroke-width="3.4" stroke-linecap="round" stroke-linejoin="round"/></svg>
        Irrigation
      </li>
      <li class="service-item">
        <svg class="tick-icon" viewBox="0 0 26 26"><circle cx="13" cy="13" r="10.5" fill="none" stroke="var(--white)" stroke-width="3"/><path d="M7.5 13.5 L12 18 L21 6" fill="none" stroke="var(--white)" stroke-width="3.4" stroke-linecap="round" stroke-linejoin="round"/></svg>
        Landscape Design
      </li>
      <li class="service-item">
        <svg class="tick-icon" viewBox="0 0 26 26"><circle cx="13" cy="13" r="10.5" fill="none" stroke="var(--white)" stroke-width="3"/><path d="M7.5 13.5 L12 18 L21 6" fill="none" stroke="var(--white)" stroke-width="3.4" stroke-linecap="round" stroke-linejoin="round"/></svg>
        Installation
      </li>
      <li class="service-item">
        <svg class="tick-icon" viewBox="0 0 26 26"><circle cx="13" cy="13" r="10.5" fill="none" stroke="var(--white)" stroke-width="3"/><path d="M7.5 13.5 L12 18 L21 6" fill="none" stroke="var(--white)" stroke-width="3.4" stroke-linecap="round" stroke-linejoin="round"/></svg>
        Well Pump
      </li>
      <li class="service-item">
        <svg class="tick-icon" viewBox="0 0 26 26"><circle cx="13" cy="13" r="10.5" fill="none" stroke="var(--white)" stroke-width="3"/><path d="M7.5 13.5 L12 18 L21 6" fill="none" stroke="var(--white)" stroke-width="3.4" stroke-linecap="round" stroke-linejoin="round"/></svg>
        Drainage Systems
      </li>
    </ul>

    <section class="contact-block">
      <p class="license-line">State Certified License #648207315</p>
      <p class="contact-line">555-316-7024 &nbsp;·&nbsp; <span class="web">Cfglawnworks.example</span></p>
      <p class="rating-line">Highly rated on Seekwell &amp; Brenda’s Roster!</p>
    </section>
  </main>
</body>
</html>
```